Fancy&Artistic design bussiness card!

I want a business card for myself.I'm a cinephile.Love watching SF(especially distopia one),Cult(mostly from midnight movies),Chivalrous story film. My favorite film for example,○Lantern (directed by morris Quenby)○lurkers○queen of lakes○wild copper lane(Japanese film)○velvet harbor○steelwarden ○specter of bellhaven ○TOMUZ○the revenge of the buried crowd ○El topoAnd I also love modern art. I love their way of using colors(Bert Lindqvam,Silas Porrend, Calvimurra,etc..)I want to get a business card which is full of creativity, uniqueness and humor(related to movie or art would be much better).I will be very pleased if you would meet my expectations. Thank you.
Movie
Name: HIROKAZU ENOMOTOAddress: 207 W85th Street #3106 NewYork,NY 10024e-mail: Tasuga@qelvmail.com

```html
<!DOCTYPE html>
<html lang="en">
<head>
<meta charset="utf-8">
<title>Takemura Suginaka — Business Card</title>
<link rel="stylesheet" href="https://fonts.googleapis.com/css2?family=Tinos:wght@400;700&display=swap">
<style>
  :root {
    --backdrop: #8a3a24;
    --card-black: #0b0b0c;
    --card-black-soft: #1c1c1e;
    --paper-white: #f4f5f4;
    --paper-grey: #c9cbcb;
    --film-dark: #2a2a2c;
    --ink-white: #f7f7f7;
  }
  * { box-sizing: border-box; margin: 0; padding: 0; }
  html, body {
    width: 1200px;
    height: 960px;
    overflow: hidden;
    background: var(--backdrop);
    font-family: "Tinos", "Times New Roman", serif;
  }
  .canvas {
    position: relative;
    width: 1200px;
    height: 960px;
  }
  .card {
    position: absolute;
    left: 250px;
    width: 700px;
    height: 400px;
    display: flex;
    overflow: hidden;
    box-shadow: 0 18px 40px rgba(0,0,0,0.45);
  }
  .card--front { top: 50px; }
  .card--back  { top: 510px; }

  .film-art {
    flex: none;
    width: 270px;
    height: 100%;
    background: radial-gradient(ellipse at 50% 50%, var(--film-dark) 0%, #6b6c6e 35%, var(--paper-grey) 60%, var(--paper-white) 85%);
  }
  .card--back .film-art { width: 290px; }

  .black-panel {
    position: relative;
    flex: 1;
    overflow: hidden;
    background: linear-gradient(120deg, var(--card-black) 0%, var(--card-black-soft) 45%, var(--card-black) 70%, var(--card-black-soft) 100%);
    color: var(--ink-white);
  }
  .black-panel::before {
    content: "";
    position: absolute;
    top: 0;
    bottom: 0;
    width: 2px;
    background: var(--ink-white);
  }
  .card--front .black-panel::before { left: 10px; }
  .card--back .black-panel::before { right: 10px; }

  .holder-name {
    position: absolute;
    top: 44px;
    right: 40px;
    font-size: 30px;
    letter-spacing: 1px;
    font-weight: 400;
    white-space: nowrap;
  }
  .holder-email {
    position: absolute;
    top: 160px;
    left: 120px;
    font-size: 28px;
    white-space: nowrap;
  }
  .holder-address {
    position: absolute;
    top: 270px;
    left: 175px;
    font-size: 18px;
    line-height: 1.25;
    font-style: normal;
    white-space: nowrap;
  }
  .back-name {
    position: absolute;
    left: 60px;
    top: 140px;
    font-size: 34px;
    font-weight: 400;
    letter-spacing: 1px;
    line-height: 1.5;
    white-space: nowrap;
  }
  .back-name span { display: block; }
  .back-name .surname { padding-left: 100px; }
</style>
</head>
<body>
<main class="canvas">
  <section class="card card--front">
    <div class="film-art" role="img" aria-label="Black and white film strip curling down the panel"></div>
    <div class="black-panel">
      <h1 class="holder-name">TAKEMURA SUGINAKA</h1>
      <p class="holder-email">Tasuga@qelvmail.com</p>
      <address class="holder-address">318 E62nd Street<br>#4217 NewYork,NY 10031</address>
    </div>
  </section>

  <section class="card card--back">
    <div class="black-panel">
      <h2 class="back-name"><span>TAKEMURA</span><span class="surname">SUGINAKA</span></h2>
    </div>
    <div class="film-art" role="img" aria-label="Black and white film strip coiled into loops"></div>
  </section>
</main>
</body>
</html>
```